New local Orchid nursery branding

We need a business card designed for our small local company in Darwin, Australia that grows orchids, called Blooms at Carrow.
We will be running private sales from our property, and handing these out at local events for perspective customers.

We would like to see designs that are simple, and able to be used with minimal colours and containing an orchid, preferably a stylised representation instead of a photo.
The eventual hope is to take this into larger formats to create our company logo/branding etc, but for now we just need business cards.

Target Market(s)

Local Orchid

Industry/Entity Type

Business

Contact Information for Business Card

Company Name
Logo
Name
Phone Number
Street Address
Email Address (less prominent than rest of the text)

Font styles to use
Sans Serif

Requirements
Must have
• Name of the company, which is Blooms at Carrow
Nice to have
• stylised orchid logo
Should not have
• too many colours

```html
<!DOCTYPE html>
<html lang="en">
<head>
<meta charset="utf-8">
<title>Blooms at Carrow – Business Card</title>
<link href="https://fonts.googleapis.com/css2?family=Montserrat:wght@700&family=Open+Sans:wght@400&display=swap" rel="stylesheet">
<style>
  :root {
    --backdrop: #ecebe8;
    --card: #ffffff;
    --navy: #1b2740;
    --teal: #1e9fbf;
    --teal-faint: rgba(30, 159, 191, 0.16);
  }
  * { margin: 0; padding: 0; box-sizing: border-box; }
  html, body {
    width: 1200px;
    height: 1023px;
    overflow: hidden;
    background: var(--backdrop);
  }
  .business-card {
    position: absolute;
    left: 150px;
    top: 254px;
    width: 900px;
    height: 514px;
    background: var(--card);
    border-radius: 40px;
    overflow: hidden;
    box-shadow: 0 10px 30px rgba(0, 0, 0, 0.12);
  }
  .brand {
    position: absolute;
    left: 60px;
    top: 150px;
    width: 360px;
    display: flex;
    flex-direction: column;
    align-items: center;
    gap: 22px;
  }
  .brand-mark {
    width: 110px;
    height: 110px;
    border-radius: 50%;
    background: var(--teal);
  }
  .brand-name {
    font-family: 'Montserrat', sans-serif;
    font-weight: 700;
    font-size: 34px;
    letter-spacing: 0.5px;
    color: var(--navy);
    text-transform: uppercase;
    white-space: nowrap;
  }
  .faint-accent {
    position: absolute;
    right: -90px;
    top: -60px;
    width: 380px;
    height: 380px;
    border-radius: 50%;
    border: 16px solid var(--teal-faint);
  }
  .contact {
    position: absolute;
    left: 480px;
    top: 120px;
    font-family: 'Open Sans', sans-serif;
    color: var(--teal);
    font-size: 21px;
    line-height: 1.5;
  }
  .contact-name {
    font-family: 'Montserrat', sans-serif;
    font-weight: 700;
    font-size: 28px;
    color: var(--navy);
    text-transform: uppercase;
    line-height: 1.2;
  }
  .contact-role { margin-bottom: 6px; }
  .contact-line {
    display: flex;
    align-items: center;
    gap: 10px;
  }
  .contact-line svg { flex: none; }
  .contact-email { font-size: 19px; }
</style>
</head>
<body>
  <main class="business-card">
    <div class="faint-accent" aria-hidden="true"></div>

    <section class="brand">
      <div class="brand-mark" aria-hidden="true"></div>
      <div class="brand-name">Blooms at Carrow</div>
    </section>

    <section class="contact">
      <div class="contact-name">Dana Whitlock</div>
      <div class="contact-role">Director</div>
      <div class="contact-line">
        <svg width="18" height="18" viewBox="0 0 24 24" aria-hidden="true">
          <path fill="#1b2740" d="M6.6 10.8a15.1 15.1 0 0 0 6.6 6.6l2.2-2.2a1 1 0 0 1 1-.25 11.4 11.4 0 0 0 3.6.6 1 1 0 0 1 1 1V20a1 1 0 0 1-1 1A17 17 0 0 1 3 4a1 1 0 0 1 1-1h3.5a1 1 0 0 1 1 1c0 1.25.2 2.45.6 3.6a1 1 0 0 1-.25 1z"/>
        </svg>
        <span>0400 555 283</span>
      </div>
      <div class="contact-line contact-email">
        <svg width="18" height="14" viewBox="0 0 24 18" aria-hidden="true">
          <rect x="1" y="1" width="22" height="16" rx="2" fill="#1b2740"/>
          <path d="M2 3l10 7 10-7" fill="none" stroke="#ffffff" stroke-width="1.8"/>
        </svg>
        <span>dwhitlock@bloomsatcarrow.com.au</span>
      </div>
      <div class="contact-address">BCom, 12 Larrakia Way<br>Rapid Creek, NT 0810</div>
    </section>
  </main>
</body>
</html>
```